Cleaning Bochure for Different Services

We need to create preferably an A4 brochure for cleaning services so we are able to give to our customers upon meeting them. check out our website for more info. It is www.brightvalecare.co.uk We need a page on;-Commercial Cleaning-Carpet Cleaning-Oven Cleaning with description and some imagery.

Target Market(s)

Commercial Cleaning Customers

Industry/Entity Type

Office Cleaning

Font styles to use
Sans Serif

Colors
33a6d7
aaaaaa

Requirements
Must have
• 4 pages each containing these services
• -Commercial Cleaning (most important)
• -Carpet Cleaning
• -Oven Cleaning
Nice to have
• Clean and smart looking design use some imagination and possibly go wild!
• Must be eye catching!

```html
<!DOCTYPE html>
<html lang="en">
<head>
<meta charset="utf-8">
<title>Brightvale Care – Brochure Pages</title>
<link rel="stylesheet" href="https://fonts.googleapis.com/css2?family=Nunito:wght@700;800&family=Questrial&display=swap">
<style>
  :root {
    --brand-blue: #1770c9;
    --sky: #4fcdf0;
    --sky-soft: #33a6d7;
    --mist: #d4dcde;
    --stone: #a3adb0;
    --ink: #2b2b2b;
    --navy: #2a3590;
    --paper: #ffffff;
  }
  * { box-sizing: border-box; margin: 0; padding: 0; }
  html, body { width: 898px; height: 1200px; overflow: hidden; background: var(--paper); }
  body { position: relative; font-family: "Questrial", sans-serif; color: var(--ink); }

  .page-tab {
    position: absolute; left: 0; width: 103px;
    background: var(--brand-blue); border: 1px solid var(--sky);
    color: var(--paper); font-family: "Nunito", sans-serif; font-weight: 800;
    font-size: 25px; padding: 66px 0 0 11px;
  }
  .page-tab--one { top: 0; height: 576px; }
  .page-tab--two { top: 622px; height: 578px; }

  .side-label { position: absolute; font-size: 17px; color: #111; font-family: "Questrial", sans-serif; }

  .panel { position: absolute; width: 373px; height: 526px; background: var(--brand-blue); border: 1px solid var(--sky); overflow: hidden; }
  .panel__shape { position: absolute; inset: 0; width: 100%; height: 100%; }
  .panel > * { position: absolute; }

  .title-band { left: 22px; top: 46px; font-family: "Nunito", sans-serif; font-weight: 800; font-size: 25px; letter-spacing: .4px; color: var(--sky); white-space: nowrap; }
  .section-title { left: 18px; top: 101px; font-size: 18px; color: var(--brand-blue); white-space: nowrap; }
  .section-lead { left: 20px; top: 126px; font-size: 9.6px; line-height: 12px; color: var(--sky); }

  .body-copy { left: 21px; width: 310px; font-size: 6.8px; line-height: 8.2px; }
  .body-copy p { margin-bottom: 8px; }

  .benefits { left: 22px; list-style: none; }
  .benefits li { display: flex; align-items: center; height: 22.5px; font-family: "Nunito", sans-serif; font-weight: 700; font-size: 8.4px; color: var(--brand-blue); }
  .tick { width: 28px; height: 20px; margin-right: 6px; flex: none; }

  .wordmark { font-family: "Nunito", sans-serif; font-weight: 800; color: var(--sky); line-height: .95; }
  .wordmark--hero { left: 120px; top: 78px; font-size: 40px; }
  .wordmark--footer { left: 24px; top: 408px; font-size: 31px; }

  .team-photo { left: 32px; top: 203px; width: 308px; height: 153px; background: linear-gradient(160deg, #1b3f8f 0%, #3c5c9c 45%, #7c8fa6 75%, #c9d3dc 100%); }
  .cover-title { left: 34px; top: 369px; font-size: 20px; line-height: 24px; color: var(--brand-blue); }
  .member-badge { left: 36px; top: 458px; width: 92px; height: 44px; }

  .footer-note { right: 26px; bottom: 5px; font-size: 6.6px; color: var(--paper); white-space: nowrap; }

  .price-list { left: 20px; top: 205px; width: 152px; font-size: 3.6px; line-height: 4.4px; color: #222; }
  .price-list .head { font-weight: bold; margin-bottom: 2px; }
  .price-list .group { margin-bottom: 3px; }
  .row { display: grid; grid-template-columns: 1fr 22px; }
  .row span:first-child { display: flex; }
  .row span:first-child::after { content: ""; flex: 1; border-bottom: .4px dotted #555; margin: 0 1px 1px; }
  .price-rule { left: 20px; top: 318px; width: 152px; height: 1px; background: #999; }
  .price-divider { left: 182px; top: 195px; width: 1.5px; height: 182px; background: var(--brand-blue); }
  .price-list--extras { left: 189px; top: 244px; width: 127px; }
  .price-list--extras .row { grid-template-columns: 1fr 12px; }
</style>
</head>
<body>

<div class="page-tab page-tab--one">Page 1</div>
<div class="page-tab page-tab--two">Page 2</div>

<div class="side-label" style="left:151px; top:3px;">Front</div>
<div class="side-label" style="left:532px; top:3px;">Back</div>
<div class="side-label" style="left:155px; top:626px;">Front</div>
<div class="side-label" style="left:529px; top:626px;">Back</div>

<!-- Page 1 front: cover -->
<section class="panel" style="left:130px; top:34px;">
  <svg class="panel__shape" viewBox="0 0 687 970" preserveAspectRatio="none" aria-hidden="true">
    <path fill="#d4dcde" d="M675,22 V450 C640,720 400,905 60,958 L12,958 C12,330 330,60 675,22 Z"/>
    <path fill="#ffffff" d="M627,32 V470 C590,700 380,880 60,952 C60,360 320,100 627,32 Z"/>
  </svg>
  <div class="wordmark wordmark--hero">Brightvale<br>Care</div>
  <div class="team-photo" role="img" aria-label="Photo of the cleaning team standing in front of branded vans outside the office"></div>
  <h1 class="cover-title" style="font-weight:normal;">Domestic and Commercial<br>Cleaning Services</h1>
  <svg class="member-badge" viewBox="0 0 92 44" role="img" aria-label="Trade body membership badge">
    <rect x="0" y="4" width="20" height="10" fill="#2a3590"/>
    <rect x="24" y="4" width="62" height="24" rx="3" fill="#2a3590"/>
  </svg>
</section>

<!-- Page 1 back: commercial cleaning -->
<section class="panel" style="left:509px; top:34px;">
  <svg class="panel__shape" viewBox="0 0 687 970" preserveAspectRatio="none" aria-hidden="true">
    <path fill="#d4dcde" d="M0,51 H670 V420 C650,720 420,930 17,966 V168 H0 Z"/>
    <path fill="#ffffff" d="M17,168 H632 V400 C600,690 390,900 17,953 Z"/>
  </svg>
  <h2 class="title-band">COMMERCIAL CLEANING</h2>
  <h3 class="section-title" style="font-weight:normal;">Commercial cleaning in York</h3>
  <div class="body-copy" style="top:145px;">
    <p>Paying too much for too little? Why not try Brightvale Care?</p>
    <p>We create bespoke packages to suit each individual businesses needs.</p>
    <p>Whether you require cleaning daily, weekly, fortnightly or monthly we are happy to create a bespoke package for you.</p>
    <p>Brightvale Care constantly strives to be the most efficient and effective commercial cleaning service in York. We are accustomed to managing a diverse array of accounts from large organisations to family businesses.</p>
    <p>We understand that the size of the business alone doesn’t define the nature and complexity of the cleaning tasks required. Therefore, we hold thorough discussions with operations management and carry out a cleaning requirements audit of the premises before initiating the contract.</p>
  </div>
  <ul class="benefits" style="top:289px;">
    <li><svg class="tick" viewBox="0 0 28 20" aria-hidden="true"><path d="M2,17 Q4,9 14,6" fill="none" stroke="#a3adb0" stroke-width="1.4"/><path d="M7,10 L12,16 L26,2" fill="none" stroke="#4fcdf0" stroke-width="2.6" stroke-linecap="round" stroke-linejoin="round"/></svg>Hassle free contract transfer (TUPE)</li>
    <li><svg class="tick" viewBox="0 0 28 20" aria-hidden="true"><path d="M2,17 Q4,9 14,6" fill="none" stroke="#a3adb0" stroke-width="1.4"/><path d="M7,10 L12,16 L26,2" fill="none" stroke="#4fcdf0" stroke-width="2.6" stroke-linecap="round" stroke-linejoin="round"/></svg>Value for money</li>
    <li><svg class="tick" viewBox="0 0 28 20" aria-hidden="true"><path d="M2,17 Q4,9 14,6" fill="none" stroke="#a3adb0" stroke-width="1.4"/><path d="M7,10 L12,16 L26,2" fill="none" stroke="#4fcdf0" stroke-width="2.6" stroke-linecap="round" stroke-linejoin="round"/></svg>Bespoke packages</li>
    <li><svg class="tick" viewBox="0 0 28 20" aria-hidden="true"><path d="M2,17 Q4,9 14,6" fill="none" stroke="#a3adb0" stroke-width="1.4"/><path d="M7,10 L12,16 L26,2" fill="none" stroke="#4fcdf0" stroke-width="2.6" stroke-linecap="round" stroke-linejoin="round"/></svg>Contact us today for a free no obligation quotation</li>
  </ul>
  <div class="wordmark wordmark--footer">Brightvale<br>Care</div>
</section>

<!-- Page 2 front: carpet cleaning -->
<section class="panel" style="left:126px; top:657px; width:371px; height:525px;">
  <svg class="panel__shape" viewBox="0 0 687 970" preserveAspectRatio="none" aria-hidden="true">
    <rect x="0" y="51" width="669" height="117" fill="#d4dcde"/>
    <path fill="#d4dcde" d="M630,168 H669 V380 C665,620 650,800 630,930 Z"/>
    <rect x="17" y="168" width="613" height="802" fill="#ffffff"/>
  </svg>
  <h2 class="title-band">COMMERCIAL CLEANING</h2>
  <h3 class="section-title" style="font-weight:normal;">Commercial carpet cleaning in York</h3>
  <p class="section-lead">Benefits of clean carpets in a commercial environment<br>Putting a spring back in your step.</p>
  <div class="body-copy" style="top:168px; width:318px;">
    <p>We are proud to offer meticulous commercial carpet cleaning in York and across the UK.</p>
    <p>Whether it being a bar, pub, restaurant, cinema, casino, bingo hall, office or educational facility we have the expertise to ensure your carpets are correctly cleaned.</p>
    <p>After heavy usage, carpet fibres become soiled meaning not even hovering can fix the problem.</p>
    <p>Our professional and affordable York Carpet Cleaning Service will use a selection of tailored techniques to ensure carpets are returned to pristine condition with no shrinkage and fast drying time.</p>
    <p>We know at Brightvale Care that your staff don’t like being disturbed while working, so that is why we offer evening and weekend services to suit you and your work forces’ schedule.</p>
    <p>Allowing obvious concerns for drying time, our expert carpet and upholstery cleaning team in York, ensure most carpets are dry within 1-2 hours meaning less hassle and minimal health and safety risks.</p>
  </div>
  <ul class="benefits" style="top:317px;">
    <li><svg class="tick" viewBox="0 0 28 20" aria-hidden="true"><path d="M2,17 Q4,9 14,6" fill="none" stroke="#a3adb0" stroke-width="1.4"/><path d="M7,10 L12,16 L26,2" fill="none" stroke="#4fcdf0" stroke-width="2.6" stroke-linecap="round" stroke-linejoin="round"/></svg>Zero Shrinkage</li>
    <li><svg class="tick" viewBox="0 0 28 20" aria-hidden="true"><path d="M2,17 Q4,9 14,6" fill="none" stroke="#a3adb0" stroke-width="1.4"/><path d="M7,10 L12,16 L26,2" fill="none" stroke="#4fcdf0" stroke-width="2.6" stroke-linecap="round" stroke-linejoin="round"/></svg>Fast drying time</li>
    <li><svg class="tick" viewBox="0 0 28 20" aria-hidden="true"><path d="M2,17 Q4,9 14,6" fill="none" stroke="#a3adb0" stroke-width="1.4"/><path d="M7,10 L12,16 L26,2" fill="none" stroke="#4fcdf0" stroke-width="2.6" stroke-linecap="round" stroke-linejoin="round"/></svg>Increases life of carpets</li>
  </ul>
  <div class="wordmark wordmark--footer">Brightvale<br>Care</div>
  <p class="footer-note" style="color:var(--brand-blue); right:32px;">Contact us today for a free no obligation quotation</p>
</section>

<!-- Page 2 back: oven cleaning -->
<section class="panel" style="left:506px; top:657px; width:372px; height:525px;">
  <svg class="panel__shape" viewBox="0 0 687 970" preserveAspectRatio="none" aria-hidden="true">
    <rect x="0" y="51" width="669" height="117" fill="#d4dcde"/>
    <path fill="#d4dcde" d="M630,168 H669 V380 C665,620 650,800 630,930 Z"/>
    <rect x="17" y="168" width="613" height="802" fill="#ffffff"/>
  </svg>
  <h2 class="title-band">OVEN CLEANING</h2>
  <h3 class="section-title" style="font-weight:normal;">Oven cleaning in York</h3>
  <p class="section-lead">In partnership with Oven Renew.</p>
  <div class="body-copy" style="top:158px; width:318px;">
    <p>Tenants landlords and agents alike.<br>Yorkshires leading oven cleaning and repair specialists. Have your oven cleaned from as little as £45.00 (inc vat)!</p>
  </div>

  <div class="price-list">
    <p class="head">UP TO 28% OFF - THE MORE WE CLEAN, THE MORE YOU SAVE!<br>(prices include VAT)</p>
    <p class="group">Standard Width Ovens (60cm):</p>
    <div class="group">
      <div class="row"><span>Single Door Oven £45</span><span>(SAVE £5)</span></div>
      <div class="row"><span>+ Hob £56</span><span>(SAVE £11)</span></div>
      <div class="row"><span>+ Extractor £56</span><span>(SAVE £11)</span></div>
      <div class="row"><span>+ Hob AND Extractor £65</span><span>(SAVE £23)</span></div>
    </div>
    <div class="group">
      <div class="row"><span>Single &amp; Grill above (Double Oven) £55</span><span>(SAVE £5)</span></div>
      <div class="row"><span>+ Hob £66</span><span>(SAVE £11)</span></div>
      <div class="row"><span>+ Extractor £66</span><span>(SAVE £11)</span></div>
      <div class="row"><span>+ Hob AND Extractor £75</span><span>(SAVE £23)</span></div>
    </div>
    <p class="group">Ranges/Wide Ovens over the standard 60cm:</p>
    <div class="group">
      <div class="row"><span>Single Door (Including FREE Hob) £74</span><span>(SAVE £25)</span></div>
      <div class="row"><span>+ Extractor £89</span><span>(SAVE £40)</span></div>
    </div>
    <div class="group">
      <div class="row"><span>Double Door (Including FREE Hob) £79</span><span>(SAVE £25)</span></div>
      <div class="row"><span>+ Extractor £89</span><span>(SAVE £40)</span></div>
    </div>
    <div class="group">
      <div class="row"><span>Triple or Four Door (Including FREE Hob) £84</span><span>(SAVE £25)</span></div>
      <div class="row"><span>+ Extractor £94</span><span>(SAVE £45)</span></div>
    </div>
    <p class="group" style="margin-top:8px;">SUPER-SAVER WHOLE KITCHEN OFFER:</p>
    <p class="group">Have ABSOLUTELY EVERYTHING below cleaned and save up to £149!!</p>
    <p>ANY Oven or Range<br>+ Hob and Hood<br>+ Microwave/Combi-Oven</p>
    <div class="row"><span>+ all white goods listed below (5 max)</span><span>JUST £139</span></div>
  </div>
  <div class="price-rule"></div>
  <div class="price-divider"></div>

  <div class="price-list price-list--extras">
    <p class="head" style="margin-bottom:6px;">PRICES FOR EXTRA ITEMS BOOKED INDIVIDUALLY:*</p>
    <div class="group">
      <div class="row"><span>Microwave</span><span>£34</span></div>
      <div class="row"><span>Combi-Oven</span><span>£46</span></div>
    </div>
    <div class="group" style="margin-top:6px;">
      <div class="row"><span>Washing Machine De-scale</span><span>£12</span></div>
      <div class="row"><span>Fridge Clean/Deodorize/Anti-Bac</span><span>£22</span></div>
      <div class="row"><span>Freezer Defrost/Clean/Deodorize/Anti-Bac</span><span>£22</span></div>
      <div class="row"><span>Dishwasher Clean/Deodorize/Anti-Bac</span><span>£12</span></div>
      <div class="row"><span>Tumble Drier Clean/De-fluff</span><span>£12</span></div>
      <p>*Individual prices valid with oven clean booking only</p>
    </div>
  </div>

  <div class="wordmark wordmark--footer">Brightvale<br>Care</div>
  <p class="footer-note" style="color:var(--brand-blue); right:32px;">Contact us today for a free no obligation quotation</p>
</section>

</body>
</html>
```